Velvet Harbor Nose Picks - our own unique product line of cotton swabs

We have something now that we are not too happy with. Looking to create a label for a line of cotton swabs that we have created and designed to clean your nose from mucus and boogers. The logo that i have so far for the packaging is the white background with the black silhouette nose (attached). We need something that can do well in the retail/consumer market. Our website address (even though it is not live yet) should be listed somewhere on the label....
www.VelvetHarbor-example.com ( we sell pillows, but we have other product lines)
We would also like to see a brief description on how to correctly use the nose pick on the back side of the label. The description on how to use should read " insert cotton nose pick into nostril and give it a few counter clock wise twirls or till you feel mucus/debris latch onto the cotton. You may need to repeat the process and use more than one nose pick to achieve desired result."
As well as a warning mentioning : "Never insert plastic end of nose pick into any part of your body. Be careful and use with caution."
Also for you to know, the cotton is made from 100% natural cotton, the cotton head itself is thick and highly absorbent making it a pleasure to use. There are 50 nose picks per pack.
We're fine with keeping it simple and not making the packaging too busy, however we're open to your ideas and designs! I have given you the most important information relevant to the project. If there are any questions or something is not clear enough please kindly message me.

Requirements
Must have
• professional looking
clean looking
not busy
Should not have
• words clumping together making it appear as too much text in one area
too much text clumped together on the design

```html
<!DOCTYPE html>
<html lang="en">
<head>
<meta charset="utf-8">
<title>Velvet Harbor Nose Picks – Labels</title>
<link href="https://fonts.googleapis.com/css2?family=Open+Sans:wght@700;800&family=Arimo:wght@400&display=swap" rel="stylesheet">
<style>
  :root {
    --ink: #111111;
    --paper: #ffffff;
    --canvas: #f4f5f6;
    --label-edge: #d9dbde;
  }
  * { box-sizing: border-box; margin: 0; padding: 0; }
  html, body { width: 1200px; height: 932px; overflow: hidden; }
  body {
    background: var(--canvas);
    position: relative;
    font-family: "Arimo", Arial, sans-serif;
    color: var(--ink);
  }

  /* Front label */
  .front-seal {
    position: absolute;
    left: 238px; top: 292px;
    width: 184px; height: 184px;
    border-radius: 50%;
    background: var(--paper);
    display: flex; align-items: center; justify-content: center;
  }
  .front-label {
    position: absolute;
    left: 186px; top: 420px;
    width: 289px; height: 205px;
    background: var(--paper);
    border-radius: 14px;
    box-shadow: 0 1px 3px rgba(0,0,0,.12);
    border: 1px solid var(--label-edge);
    text-align: center;
    padding-top: 26px;
  }
  .brand-name {
    font-family: "Open Sans", Arial, sans-serif;
    font-weight: 800;
    font-size: 31px;
    letter-spacing: -0.5px;
    line-height: 1.1;
  }
  .swab-rule { display: block; margin: 16px auto 4px; }
  .product-type {
    font-size: 15px;
    letter-spacing: 5px;
    margin-top: 2px;
  }
  .pack-count {
    font-family: "Open Sans", Arial, sans-serif;
    font-weight: 700;
    font-size: 16px;
    margin-top: 18px;
  }

  /* Back label */
  .back-label {
    position: absolute;
    left: 727px; top: 360px;
    width: 288px; height: 303px;
    background: var(--paper);
    border-radius: 14px;
    box-shadow: 0 1px 3px rgba(0,0,0,.12);
    border: 1px solid var(--label-edge);
    padding: 16px 18px 0 19px;
  }
  .back-title {
    font-family: "Open Sans", Arial, sans-serif;
    font-weight: 700;
    font-size: 21px;
    text-align: center;
    margin-bottom: 9px;
  }
  .usage, .warning {
    font-size: 14.6px;
    line-height: 17px;
  }
  .warning { margin-top: 22px; }
  .web-address {
    font-family: "Open Sans", Arial, sans-serif;
    font-weight: 700;
    font-size: 14.5px;
    text-align: center;
    margin-top: 18px;
  }
</style>
</head>
<body>

  <div class="front-seal">
    <svg width="144" height="144" viewBox="0 0 144 144" role="img" aria-label="Natural cotton quality seal">
      <circle cx="72" cy="72" r="70" fill="var(--ink)"/>
      <circle cx="72" cy="72" r="58" fill="var(--paper)"/>
      <circle cx="72" cy="72" r="40" fill="none" stroke="var(--ink)" stroke-width="3"/>
    </svg>
  </div>

  <section class="front-label">
    <h1 class="brand-name">Velvet Harbor</h1>
    <svg class="swab-rule" width="230" height="16" viewBox="0 0 230 16" aria-hidden="true">
      <ellipse cx="14" cy="8" rx="12" ry="6" fill="none" stroke="var(--ink)" stroke-width="1.5"/>
      <line x1="26" y1="8" x2="40" y2="5" stroke="var(--ink)" stroke-width="1.5"/>
      <line x1="40" y1="5" x2="230" y2="5" stroke="var(--ink)" stroke-width="3"/>
    </svg>
    <p class="product-type">Cotton Sticks</p>
    <p class="pack-count">50 nose picks</p>
  </section>

  <section class="back-label">
    <h2 class="back-title">100% natural cotton</h2>
    <p class="usage">Insert cotton nose pick into nostril and give it a few counter clock wise twirls or till you feel mucus/ debris latch onto the cotton. You may need to repeat the process and use more than one nose pick to achieve desired result.</p>
    <p class="warning">Never insert plastic end of nose pick into any part of your body. Be careful and use with caution.</p>
    <p class="web-address">www.VelvetHarbor-example.com</p>
  </section>

</body>
</html>
```